Painting Contractor Business Card Design

We are looking for a cool, bold, modern, polished, business card design. We are a high-end residential painting contractor. Please incorporate our logo and keep with our green/black color scheme. We are interested in seeing 2-sided and 1-sided options. Thank you very much!

Industry/Entity Type

Business

Contact Information for Business Card

Info for the card:
Owen Talsky
mobile 206-555-0193
email owen@kestrowfinish.net
web www.kestrowfinish.net

```html
<!DOCTYPE html>
<html lang="en">
<head>
<meta charset="utf-8">
<title>Kestrow Finish – Business Card</title>
<link rel="stylesheet" href="https://fonts.googleapis.com/css2?family=Questrial&family=Montserrat:wght@600&display=swap">
<style>
  :root {
    --stage: #d9d9d9;
    --card-black: #111212;
    --card-black-soft: #1d1e1e;
    --panel-edge: #2c2d2d;
    --green: #5fae3c;
    --green-deep: #3f8a2a;
    --green-light: #7ccb4e;
    --white: #f2f2f2;
  }
  * { margin: 0; padding: 0; box-sizing: border-box; }
  html, body {
    width: 1200px; height: 873px; overflow: hidden;
    background: var(--stage);
  }
  .stage {
    position: relative; width: 1200px; height: 873px;
    background: linear-gradient(180deg, #e4e4e4 0%, var(--stage) 100%);
    font-family: "Questrial", sans-serif;
  }
  .card {
    position: absolute; overflow: hidden;
    background: var(--card-black);
    box-shadow: 0 10px 28px rgba(0,0,0,0.28);
  }

  /* Back side – horizontal */
  .card--back { left: 85px; top: 256px; width: 630px; height: 360px; }
  .back-texture {
    position: absolute; inset: 0;
    background: linear-gradient(155deg, var(--card-black-soft) 0%, var(--card-black) 55%, #161717 100%);
  }
  .back-block {
    position: absolute; left: 372px; top: 78px; width: 300px; height: 300px;
    background: linear-gradient(150deg, var(--green-light) 0%, var(--green) 45%, var(--green-deep) 100%);
    border: 6px solid var(--panel-edge);
  }
  .back-web {
    position: absolute; left: 78px; top: 166px;
    font-size: 17px; letter-spacing: 0.3px; color: var(--green-light);
  }

  /* Front side – vertical */
  .card--front {
    left: 755px; top: 121px; width: 360px; height: 630px;
    background: linear-gradient(170deg, var(--card-black-soft) 0%, var(--card-black) 60%);
  }
  .brand {
    position: absolute; left: 0; right: 0; top: 150px;
    display: flex; justify-content: center; align-items: center; gap: 12px;
  }
  .brand-mark { width: 18px; height: 18px; background: var(--green); }
  .brand-name { font-size: 26px; letter-spacing: 1.5px; color: var(--white); }
  .person-name {
    position: absolute; left: 0; right: 0; top: 346px; text-align: center;
    font-family: "Montserrat", sans-serif; font-weight: 600;
    font-size: 25px; color: var(--white);
  }
  .contact {
    position: absolute; left: 0; right: 0; top: 460px; text-align: center;
    list-style: none; color: var(--green-light); font-size: 16px; line-height: 25px;
  }
  .contact .contact-web { font-weight: 700; }
  .edge-tab {
    position: absolute; right: 0; width: 22px; height: 40px;
    background: var(--green); border: 2px solid var(--panel-edge); border-right: none;
  }
  .edge-tab--top { top: 346px; }
  .edge-tab--mid { top: 466px; }
  .edge-tab--low { top: 590px; }
</style>
</head>
<body>
<main class="stage">

  <section class="card card--back" aria-label="Card back">
    <div class="back-texture" role="img" aria-label="Dark faceted line pattern across the card back"></div>
    <span class="back-block" aria-hidden="true"></span>
    <p class="back-web">www.kestrowfinish.net</p>
  </section>

  <section class="card card--front" aria-label="Card front">
    <div class="brand">
      <span class="brand-mark" aria-hidden="true"></span>
      <span class="brand-name">KESTROW FINISH</span>
    </div>
    <h1 class="person-name">Owen Talsky</h1>
    <ul class="contact">
      <li>206-555-0193</li>
      <li>owen@kestrowfinish.net</li>
      <li class="contact-web">www.kestrowfinish.net</li>
    </ul>
    <span class="edge-tab edge-tab--top" aria-hidden="true"></span>
    <span class="edge-tab edge-tab--mid" aria-hidden="true"></span>
    <span class="edge-tab edge-tab--low" aria-hidden="true"></span>
  </section>

</main>
</body>
</html>
```